Firm of surveyors needs a professional yet friendly looking flyer

Our company offers help to landlords who have a phone mast on their property. We help them to negotiate the best rent and lease terms. There are so many landlords who don't seek professional advice because they don't know it's available. We want to send them a flyer which is informative, looks professional but also friendly so it prompts them to call us. I have attached the wording and some pictures but have more I can send but they were too large to attach.

Target Market(s)

Ranges from farmers to large corporations and land owners

Industry/Entity Type

Surveyor

Font styles to use
Sans Serif

Colors
acd136
9bcb3c
000000
ffffff
606060
848484

Requirements
Must have
• Must be clear, must give a professional look, must include pictures, must include our logo, must use our colour scheme (or variations of it). Ideally, I would like a try-fold design if possible.
Nice to have
• I would like there to be stand out lines to catch the readers eye (I have included some on the wording document). I would like a clean and modern design
Should not have
• Should not be too fussy

```html
<!DOCTYPE html>
<html lang="en">
<head>
<meta charset="utf-8">
<title>The Signal Lease Company – Flyer</title>
<link rel="stylesheet" href="https://fonts.googleapis.com/css2?family=Source+Sans+3:wght@400;600;700;800&display=swap">
<style>
  :root {
    --green-light: #8cc63f;
    --green-bright: #acd136;
    --green-mid: #9bcb3c;
    --green-dark: #3c5a22;
    --green-deep: #2c4419;
    --ink: #000000;
    --white: #ffffff;
    --grey: #606060;
    --grey-light: #848484;
    --body-bg: #1d1f1f;
    --sky-top: #2f77c2;
    --sky-bottom: #a9cbe8;
    --steel: #c9d2da;
  }
  * { box-sizing: border-box; margin: 0; padding: 0; }
  html, body { width: 776px; height: 1200px; overflow: hidden; background: var(--white); }
  body { font-family: "Source Sans 3", "Myriad Pro", Arial, sans-serif; }
  .flyer { position: relative; width: 776px; height: 1200px; overflow: hidden; background: var(--body-bg); }

  .hero-photo {
    position: absolute; left: 0; top: 0; width: 776px; height: 470px;
    background:
      radial-gradient(ellipse 170px 230px at 380px 250px, rgba(220,228,235,0.95) 0%, rgba(170,185,200,0.75) 45%, rgba(120,160,205,0) 100%),
      radial-gradient(ellipse 260px 120px at 130px 150px, rgba(255,255,255,0.45) 0%, rgba(255,255,255,0) 100%),
      radial-gradient(ellipse 300px 140px at 600px 330px, rgba(255,255,255,0.45) 0%, rgba(255,255,255,0) 100%),
      linear-gradient(180deg, var(--sky-top) 0%, #5f9bd4 55%, var(--sky-bottom) 100%);
  }

  .circuit-bg {
    position: absolute; left: 0; top: 575px; width: 776px; height: 625px;
    background:
      radial-gradient(ellipse 400px 260px at 620px 420px, rgba(70,75,75,0.45) 0%, rgba(0,0,0,0) 100%),
      linear-gradient(180deg, #1b1d1d 0%, #242626 60%, #1a1c1c 100%);
  }

  .brand-panel { position: absolute; left: 405px; top: 56px; width: 371px; height: 150px; }
  .brand-name {
    position: absolute; left: 524px; top: 100px; width: 230px;
    font-weight: 800; font-size: 27px; line-height: 1.0; color: var(--green-dark);
  }
  .brand-dot {
    position: absolute; left: 494px; top: 110px; width: 20px; height: 20px;
    border-radius: 50%; background: var(--green-dark);
  }

  .bands { position: absolute; left: 0; top: 370px; width: 776px; height: 210px; }

  .headline {
    position: absolute; left: 20px; top: 467px; width: 610px;
    text-align: center; color: var(--white);
    font-weight: 700; font-size: 23px; line-height: 30px;
  }

  .copy { position: absolute; left: 78px; width: 622px; color: var(--white); }
  .intro { top: 596px; font-weight: 700; font-size: 20px; line-height: 28px; text-align: justify; }
  .body-text { font-size: 19.5px; line-height: 24px; text-align: justify; font-weight: 400; }
  .about { top: 708px; }
  .sell { top: 949px; line-height: 26px; }

  .section-tab { position: absolute; left: 0; top: 896px; width: 425px; height: 42px; }
  .section-title {
    position: absolute; left: 78px; top: 902px;
    font-weight: 700; font-size: 22px; line-height: 30px; color: var(--white);
  }
</style>
</head>
<body>
<main class="flyer">
  <div class="hero-photo" role="img" aria-label="Photo: mobile phone mast with antennas and dishes against a blue cloudy sky"></div>
  <div class="circuit-bg" role="img" aria-label="Dark circuit board texture background"></div>

  <svg class="brand-panel" viewBox="0 0 371 150" aria-hidden="true">
    <polygon points="14,10 371,10 371,150 56,150" fill="#27476e" opacity="0.55"/>
    <polygon points="10,4 371,4 371,144 52,144" fill="var(--white)"/>
  </svg>
  <span class="brand-dot" aria-hidden="true"></span>
  <div class="brand-name">The Signal Lease Company</div>

  <svg class="bands" viewBox="0 0 776 210" aria-hidden="true">
    <polygon points="0,92 612,92 776,14 776,70 612,165 0,165" fill="var(--green-light)"/>
    <polygon points="0,165 612,165 776,70 776,130 612,205 0,205" fill="var(--green-deep)"/>
    <polygon points="612,165 776,70 776,100 612,185" fill="var(--green-dark)"/>
  </svg>

  <h1 class="headline">Unsure whether you are getting the best rent?<br>Call us now for a free, no obligation chat</h1>

  <p class="copy intro">The Signal Lease Company is a firm of telecoms surveyors with over 15 years’ experience of dealing with mobile phone mast operators.</p>

  <p class="copy body-text about">We have built up a massive database of thousands of comparable mobile phone mast deals to aid us in our telecoms negotiations. All our surveyors have spent time working for phone mast operators and know the industry inside out. We now work exclusively for landlords, fighting your corner, ensuring our landlords get the highest rents and best lease terms available in the market place.</p>

  <svg class="section-tab" viewBox="0 0 425 42" aria-hidden="true">
    <polygon points="0,0 385,0 425,42 0,42" fill="var(--green-light)"/>
  </svg>
  <h2 class="section-title">Sell your phone mast</h2>

  <p class="copy body-text sell">We can also assist landlords in selling their phone mast. We have strong links with many large investors who regularly purchase the freehold or leasehold interest of masts and will pay a cash lump sum of tens, even hundreds of thousands of pounds. This can be done in a matter of weeks and the cash is yours to spend however you like, regardless of whether the mast stays for the duration of the investors leasehold or not. We can negotiate flexible terms, such as a buyback option so please call us today to discuss.</p>
</main>
</body>
</html>
```